依頼詳細
[ 歯科医院の特徴 ]
◆ ターゲット層
30代〜40代の女性がメインターゲット

派生してお子さんや年配の方までが通いやすい、
『家族で通えるような歯科医院』

◆ 推していく診療
オールマイティな診療(総合歯科診療)を行いつつ、
予防歯科・矯正歯科(Vuxa有り)・CAD/CAM(ミロナ)の患者を獲得。

◆ サイトで伝えていきたいこと
予防歯科の重要性
感染予防対策が行われている医院
早く、精密に行えるデジタルな診療

◆ 好きなサイトテイスト
https://www.wavelid-dentaloffice.example/

現代のサイトデザインの流行を取り入れ、
おしゃれではあるもののユーザーファーストなデザインを希望いたします。

また、Javascriptで多少のフェードインを想定しておりますので、
それに伴ったデザインを構成していただけますと幸いです。

内装パースデザイン, ロゴデザインを添付しております。
ご覧いただき、一貫性のあるサイトデザインをご提案いただけますと幸いです。

◆ 診療理念
患者様の笑顔と健康をサポートする
◇ 患者様によく説明し、納得、理解していただき歯科治療を行う
◇ 最新歯科治療、技術、サービスの日々研鑚取得
◇ 痛みの少ない治療の実施、低侵襲治療
◇ 行き届いた滅菌、衛生管理
◇ 自らの家族を呼べるような場所

◆ 医院の特徴
・可能な限り抜かない、削らない低侵襲治療(予防歯科の推奨)
・先進医療機器で治療の可能性を最大限に。
・安心して治療が受けられる衛生管理徹底
・矯正担当医によるソルテミーナ矯正・小児矯正
・患者様が通いやすい土日診療

◆ 診療時間
診療時間   月 火 水 木 金 土 日
09:30-13:00 ○ - ○ ○ ○ ○ ○
14:30-18:30 ○ - ○ ○ ○ ▲ ▲
▲:土日 (14:30-17:00)
休診日:火曜・祝日

◆ 院内紹介
①待合室
患者様に明るく広いリラックスできる空間を心がけています。

②キッズルーム
キッズルームやおむつ交換台もあるのでお子様連れのお母さんも安心です。

③完全バリアフリー設計
駐車場から治療室までバリアフリー設計になっています。ベビーカーでそのまま入れます。

④カウセリングルーム
お悩み事や診療への不安など気軽に相談ください。現在のお口の状態、治療計画、診療費用などをモニターを用いてご説明します。

⑤個室診療室
配慮したい時や、精密な治療などを行うときのために、個室診療室をご用意いたしました。静かな環境で、治療をお受けください。

⑥口腔外バキューム
歯の削りかすや血液などが空気中に飛び散るのを防ぐために口腔外バキュームを採用しております。口腔外バキュームは、口腔内バキュームの約2倍の吸収率で、粉塵を確実に吸い取ります。院内の衛生管理に、欠かせないアイテムです。
サイトURL
ページ数
1ページ
希望イメージ
シンプル 複雑
単色 カラフル
暗い 明るい
日常 高級
遊び心 厳粛
未来的 伝統的
女性的 男性的
希望する色
青系、水色系、茶系
納品ファイル
• 高解像度JPG (.jpg)
• イラストレーター形式 (.ai)
• PNG形式 (.png)
補足説明
TOPページだけでなく、SUBページもお願いできればと思い、
この度延長をいたしました。

◇ TOPページのデザイン(レスポンシブ)

◇ SUBページのテンプレートデザイン(レスポンシブ)
テンプレート化してそれを元に他ページを作成できるよう、
見出しタグや画像を使用した際のレイアウト例をお願いいたします。
[ 参考:https://www.tomorane-shika.example/sub.html ]

```html
<!DOCTYPE html>
<html lang="ja">
<head>
<meta charset="utf-8">
<title>HARE デンタルクリニック</title>
<link href="https://fonts.googleapis.com/css2?family=Noto+Sans+JP:wght@400;500;700&family=Montserrat:wght@500;600&display=swap" rel="stylesheet">
<style>
:root{
  --blue:#1f5ad8;
  --blue-dark:#1546b4;
  --sky:#dfe9fb;
  --ink:#2b2f38;
  --muted:#6b7280;
  --cream:#fbf1ec;
  --line:#d7dce6;
  --white:#fff;
}
*{margin:0;padding:0;box-sizing:border-box}
html,body{width:1200px;height:4236px;overflow:hidden}
body{font-family:"Noto Sans JP",sans-serif;color:var(--ink);background:var(--white);position:relative}
.en{font-family:"Montserrat",sans-serif;letter-spacing:.15em}

/* header */
.header{position:absolute;top:0;left:0;width:1200px;height:64px;display:flex;align-items:center;z-index:3}
.brand{display:flex;align-items:center;gap:10px;font-weight:700;font-size:18px;color:var(--white);margin-left:40px}
.brand i{width:22px;height:22px;border-radius:50%;background:var(--white);display:block}
.nav{position:absolute;left:300px;top:0;height:64px;width:740px;background:var(--white);display:flex;align-items:center;justify-content:space-around;font-size:13px;color:var(--ink)}
.reserve{position:absolute;right:0;top:0;width:160px;height:64px;background:var(--blue);color:var(--white);font-size:15px;font-weight:700;display:flex;align-items:center;justify-content:center}

/* hero */
.hero-photo{position:absolute;top:0;left:0;width:1200px;height:900px;background:linear-gradient(120deg,#b9c9e4 0%,#e3e9f1 45%,#f3f4f6 70%,#d7dde6 100%)}
.hero-title{position:absolute;left:110px;top:230px;color:var(--white);font-size:56px;font-weight:700;line-height:1.45;letter-spacing:.08em;text-shadow:0 2px 12px rgba(20,50,120,.35)}
.hero-wave{position:absolute;left:0;top:680px}

/* intro */
.intro{position:absolute;top:890px;left:0;width:1200px;text-align:center}
.intro h2{font-size:24px;font-weight:500;letter-spacing:.15em;color:var(--ink);margin-bottom:22px}
.intro p{font-size:13px;line-height:2.1;color:var(--muted);letter-spacing:.08em}

/* section head */
.sec-head{text-align:center}
.sec-head h2{font-size:30px;font-weight:700;letter-spacing:.15em}
.sec-head span{display:block;font-size:11px;margin-top:6px}

/* features */
.features{position:absolute;top:1190px;left:0;width:1200px;height:420px;background:var(--blue);color:var(--white);padding-top:44px}
.feature-list{display:flex;gap:24px;justify-content:center;margin-top:60px}
.feature-card{width:176px;height:148px;background:var(--white);border-radius:10px;color:var(--blue);text-align:center;padding-top:22px;font-size:13px;line-height:1.6;font-weight:500}
.feature-card svg{display:block;margin:0 auto 12px}

/* facility */
.facility{position:absolute;top:1650px;left:0;width:1200px}
.facility .sec-head h2{color:var(--blue)}
.facility .sec-head span{color:var(--blue)}
.room-grid{display:grid;grid-template-columns:repeat(3,300px);gap:48px 40px;justify-content:center;margin-top:56px}
.room-card{height:320px;background:var(--cream);border-radius:4px;position:relative}
.room-photo{height:168px;background:linear-gradient(135deg,#e8e2da,#f6f3ef 60%,#d9dde3)}
.room-num{position:absolute;top:0;left:0;background:var(--white);color:var(--blue);font-size:22px;font-weight:600;padding:4px 12px}
.room-card h3{font-size:15px;font-weight:500;text-align:center;margin:20px 0 10px}
.room-card p{font-size:12px;line-height:1.8;color:var(--muted);text-align:center;padding:0 36px}

/* philosophy */
.philosophy{position:absolute;top:2590px;left:0;width:1200px}
.philosophy .sec-head h2{color:var(--ink)}
.philosophy .sec-head span{color:var(--muted)}
.philo-list{display:flex;gap:22px;justify-content:center;margin-top:54px}
.philo-card{width:176px;height:210px;background:var(--blue);color:var(--white);border-radius:6px;text-align:center;padding:30px 14px 0;font-size:13px;line-height:1.7}
.philo-card svg{display:block;margin:0 auto 22px}

/* company */
.company{position:absolute;top:2980px;left:0;width:1200px;height:640px;background:var(--cream)}
.company .sec-head{padding-top:46px}
.company .sec-head h2{color:var(--ink)}
.company .sec-head span{color:var(--muted)}
.co-brand{position:absolute;left:110px;top:244px;display:flex;align-items:center;gap:10px;font-size:18px;font-weight:700;color:var(--blue);white-space:nowrap}
.co-brand i{width:28px;height:28px;border-radius:50%;background:var(--blue);display:block}
.co-address{position:absolute;left:390px;top:238px;font-size:12px;line-height:1.8;color:var(--ink)}
.info-table{position:absolute;left:110px;top:320px;font-size:12px;border-collapse:collapse}
.info-table td{padding:6px 12px 6px 0;vertical-align:top}
.info-table .lbl{font-weight:500;width:90px}
.tel-label{position:absolute;left:700px;top:216px;font-size:11px;color:var(--muted)}
.tel{position:absolute;left:700px;top:236px;font-size:22px;font-weight:600;color:var(--blue);font-family:"Montserrat",sans-serif;white-space:nowrap}
.co-reserve{position:absolute;left:910px;top:218px;width:180px;height:54px;background:var(--blue);color:var(--white);font-size:15px;font-weight:700;display:flex;align-items:center;justify-content:center;border-radius:3px}
.hours{position:absolute;left:700px;top:300px;width:390px;border-collapse:collapse;font-size:12px;text-align:center}
.hours th,.hours td{border-bottom:1px solid var(--line);padding:12px 0}
.hours th{font-weight:500}
.hours td.time{text-align:left;font-weight:500;padding-left:4px}
.dot{display:inline-block;width:8px;height:8px;border-radius:50%;background:var(--blue)}
.tri{display:inline-block;width:0;height:0;border-left:5px solid transparent;border-right:5px solid transparent;border-bottom:9px solid var(--blue)}
.hours-note{position:absolute;left:930px;top:446px;font-size:11px;color:var(--ink)}

/* recruit */
.recruit{position:absolute;top:3720px;left:170px;width:920px;height:250px;background:#f0f1f3}
.recruit-photo{position:absolute;right:0;top:0;width:560px;height:250px;background:linear-gradient(120deg,#dfe6ef,#f6f7f9 50%,#c9d6e8)}
.recruit-en{position:absolute;left:40px;top:60px;font-size:56px;color:var(--blue);font-family:"Montserrat",sans-serif;font-weight:500}
.recruit h2{position:absolute;left:60px;top:140px;font-size:22px;font-weight:700;color:var(--ink);letter-spacing:.1em}

/* footer */
.footer{position:absolute;top:4000px;left:0;width:1200px;height:236px;background:var(--blue);color:var(--white)}
.f-brand{position:absolute;left:110px;top:80px;display:flex;align-items:center;gap:10px;font-size:18px;font-weight:700}
.f-brand i{width:26px;height:26px;border-radius:50%;background:var(--white);display:block}
.f-links{position:absolute;left:420px;top:60px;display:grid;grid-template-columns:repeat(3,180px);gap:20px 0;font-size:12px}
.f-links li{list-style:none}
.f-links li::before{content:"▸ ";font-size:9px}
.social{position:absolute;right:110px;top:60px;display:flex;gap:14px}
.social i{width:18px;height:18px;border-radius:50%;background:var(--white);display:block}
.copy{position:absolute;right:110px;top:200px;font-size:10px;opacity:.8}
</style>
</head>
<body>

<header class="header">
  <div class="brand"><i></i>HARE デンタルクリニック</div>
  <nav class="nav">
    <span>クリニックのこと</span><span>医院の特長</span><span>診療案内</span><span>院内紹介</span><span>診療理念</span><span>採用情報</span>
  </nav>
  <div class="reserve">ネット予約</div>
</header>

<div class="hero-photo" role="img" aria-label="歯科医師が子どもの患者を診療している明るい診療室の写真"></div>
<h1 class="hero-title">家族の笑顔を支える<br>総合歯科医院</h1>
<svg class="hero-wave" width="1200" height="230" viewBox="0 0 1200 230"><path d="M0 120 C300 10 700 240 1200 60 L1200 230 L0 230Z" fill="#fff"/></svg>

<section class="intro">
  <h2>家族の笑顔を支える</h2>
  <p>歯のトラブルから守るお手伝いをしています。<br>大事な歯をいつまでも、健やかに保つ治療を行います。<br>大切なお子さまの笑顔を守ることを目指します。<br>私たち、HARE デンタルクリニックは地域に寄り添います。<br>早く、精密に行えるデジタル診療。<br>小さなお子さまからご年配の方まで安心して通える医院へ。<br>全ての患者さまに、ご家族のように心を込めて対応いたします。<br>HARE デンタルクリニックは、家族の笑顔を支えます。</p>
</section>

<section class="features">
  <div class="sec-head"><h2>医院の特長</h2><span class="en">FEATURES</span></div>
  <div class="feature-list">
    <div class="feature-card"><svg width="40" height="40" viewBox="0 0 40 40" fill="none" stroke="#1f5ad8" stroke-width="2"><path d="M10 8c4-3 8 0 10 0s6-3 10 0c4 4 1 12 0 16-1 5-2 10-4 10s-2-8-6-8-4 8-6 8-3-5-4-10c-1-4-4-12 0-16z"/></svg>可能な限り抜かない<br>削らない低侵襲治療<br>(予防歯科の推奨)</div>
    <div class="feature-card"><svg width="40" height="40" viewBox="0 0 40 40" fill="none" stroke="#1f5ad8" stroke-width="2"><path d="M6 34 30 10M24 6l10 10M12 28l-4-4"/></svg>先進医療機器で<br>治療の可能性を<br>最大限に</div>
    <div class="feature-card"><svg width="40" height="40" viewBox="0 0 40 40" fill="none" stroke="#1f5ad8" stroke-width="2"><path d="M20 4 34 10v10c0 8-6 13-14 16C12 33 6 28 6 20V10z"/><path d="M14 20l4 4 8-8"/></svg>安心して治療が<br>受けられる<br>衛生管理徹底</div>
    <div class="feature-card"><svg width="40" height="40" viewBox="0 0 40 40" fill="none" stroke="#1f5ad8" stroke-width="2"><rect x="4" y="12" width="14" height="16" rx="5"/><rect x="22" y="12" width="14" height="16" rx="5"/><path d="M2 20h36"/></svg>矯正担当医による<br>ソルテミーナ<br>矯正・小児矯正</div>
    <div class="feature-card"><svg width="40" height="40" viewBox="0 0 40 40" fill="none" stroke="#1f5ad8" stroke-width="2"><rect x="6" y="8" width="28" height="26" rx="2"/><path d="M6 16h28M13 4v8M27 4v8"/></svg>患者様が<br>通いやすい<br>土日診療</div>
  </div>
</section>

<section class="facility">
  <div class="sec-head"><h2>院内紹介</h2><span class="en">INTRODUCTION</span></div>
  <div class="room-grid">
    <div class="room-card"><div class="room-photo" role="img" aria-label="明るい待合室の写真"></div><span class="room-num en">01</span><h3>待合室</h3><p>患者様に明るく広いリラックスできる空間を心がけています。</p></div>
    <div class="room-card"><div class="room-photo" role="img" aria-label="子どもが遊ぶキッズルームの写真"></div><span class="room-num en">02</span><h3>キッズルーム</h3><p>キッズルームやおむつ交換台もあるのでお子様連れのお母さんも安心です。</p></div>
    <div class="room-card"><div class="room-photo" role="img" aria-label="バリアフリーの院内通路の写真"></div><span class="room-num en">03</span><h3>完全バリアフリー設計</h3><p>駐車場から治療室までバリアフリー設計になっています。ベビーカーでそのまま入れます。</p></div>
    <div class="room-card"><div class="room-photo" role="img" aria-label="カウンセリングルームで相談する様子の写真"></div><span class="room-num en">04</span><h3>カウセリングルーム</h3><p>お悩み事や診療への不安など気軽に相談ください。治療計画、診療費用などをモニターでご説明します。</p></div>
    <div class="room-card"><div class="room-photo" role="img" aria-label="個室診療室の写真"></div><span class="room-num en">05</span><h3>個室診療室</h3><p>配慮したい時や、精密な治療などを行うときのために、個室診療室をご用意いたしました。</p></div>
    <div class="room-card"><div class="room-photo" role="img" aria-label="口腔外バキューム機器の写真"></div><span class="room-num en">06</span><h3>口腔外バキューム</h3><p>歯の削りかすや血液などが空気中に飛び散るのを防ぐために口腔外バキュームを採用しております。</p></div>
  </div>
</section>

<section class="philosophy">
  <div class="sec-head"><h2>診療理念</h2><span class="en">PHILOSOPHY</span></div>
  <div class="philo-list">
    <div class="philo-card"><svg width="48" height="48" viewBox="0 0 40 40" fill="none" stroke="#fff" stroke-width="2"><path d="M10 8c4-3 8 0 10 0s6-3 10 0c4 4 1 12 0 16-1 5-2 10-4 10s-2-8-6-8-4 8-6 8-3-5-4-10c-1-4-4-12 0-16z"/></svg>患者様によく説明し、納得、理解していただき歯科治療を行う</div>
    <div class="philo-card"><svg width="48" height="48" viewBox="0 0 40 40" fill="none" stroke="#fff" stroke-width="2"><path d="M10 10c4-3 8 0 10 0s6-3 10 0c4 4 1 12 0 16-1 5-2 8-4 8s-2-6-6-6-4 6-6 6-3-3-4-8c-1-4-4-12 0-16z"/><path d="M33 2v6M30 5h6"/></svg>最新歯科治療、技術、サービスの日々研鑚取得</div>
    <div class="philo-card"><svg width="48" height="48" viewBox="0 0 40 40" fill="none" stroke="#fff" stroke-width="2"><path d="M12 6v28M20 6v28M28 6v28"/></svg>痛みの少ない治療の実施、低侵襲治療</div>
    <div class="philo-card"><svg width="48" height="48" viewBox="0 0 40 40" fill="none" stroke="#fff" stroke-width="2"><rect x="4" y="12" width="32" height="18" rx="3"/><path d="M12 12V8h16v4"/></svg>行き届いた滅菌、<br>衛生管理</div>
    <div class="philo-card"><svg width="48" height="48" viewBox="0 0 40 40" fill="none" stroke="#fff" stroke-width="2"><circle cx="13" cy="10" r="4"/><circle cx="27" cy="10" r="4"/><path d="M6 34V22a7 7 0 0 1 14 0v12M20 34V22a7 7 0 0 1 14 0v12"/></svg>自らの家族を呼べるような場所</div>
  </div>
</section>

<section class="company">
  <div class="sec-head"><h2>会社情報</h2><span class="en">COMPANY</span></div>
  <div class="co-brand"><i></i>HARE デンタルクリニック</div>
  <p class="co-address">〒100-0000<br>東京都みなと区みなと1-2-3</p>
  <table class="info-table">
    <tr><td class="lbl">診療時間</td><td>月・水・木・金</td><td>9:30 - 13:00<br>14:30 - 18:30</td></tr>
    <tr><td></td><td>土日</td><td>9:30 - 13:00<br>14:30 - 17:00</td></tr>
    <tr><td class="lbl">休診日</td><td colspan="2">火曜・祝日</td></tr>
  </table>
  <p class="tel-label">お電話でのご予約</p>
  <p class="tel">tel.000-1234-0000</p>
  <div class="co-reserve">ネット予約</div>
  <table class="hours">
    <tr><th></th><th>月</th><th>火</th><th>水</th><th>木</th><th>金</th><th>土</th><th>日</th></tr>
    <tr><td class="time">午前</td><td><span class="dot"></span></td><td>-</td><td><span class="dot"></span></td><td><span class="dot"></span></td><td><span class="dot"></span></td><td><span class="dot"></span></td><td><span class="dot"></span></td></tr>
    <tr><td class="time">午後</td><td><span class="dot"></span></td><td>-</td><td><span class="dot"></span></td><td><span class="dot"></span></td><td><span class="dot"></span></td><td><span class="tri"></span></td><td><span class="tri"></span></td></tr>
  </table>
  <p class="hours-note"><span class="tri"></span> 土日 14:30 - 17:00</p>
</section>

<section class="recruit">
  <div class="recruit-photo" role="img" aria-label="歯科スタッフが働く様子の写真"></div>
  <span class="recruit-en">Re</span>
  <h2>採用情報</h2>
</section>

<footer class="footer">
  <div class="f-brand"><i></i>HARE デンタルクリニック</div>
  <ul class="f-links">
    <li>クリニックのこと</li><li>医院の特長</li><li>診療案内</li>
    <li>院内紹介</li><li>診療理念</li><li>採用情報</li>
    <li>サイトポリシー</li><li>個人情報保護</li>
  </ul>
  <div class="social"><i></i><i></i><i></i></div>
  <p class="copy en">© HARE DENTAL CLINIC</p>
</footer>

</body>
</html>
```